New website for a commercial real estate consulting company

What we’re looking for in a new web site:
• Desktop and mobile friendly
• Clear navigation
• Strong graphics
• Professional appearance
• The ability to update it ourselves
• Site is for information purposes only – no transactions required
• Traffic counts – number of visits per page?
• A firm quote on costs to develop and launch
• SSL
Attached is a copy of the revised text we propose to use, including our new logo. (The pagination can be different than as shown.)
Our current website address is www.brightlanecounselgroup.ca

```html
<!DOCTYPE html>
<html lang="en">
<head>
<meta charset="utf-8">
<title>Brightlane Counsel Group</title>
<link href="https://fonts.googleapis.com/css2?family=Roboto:wght@300;400;500;700&display=swap" rel="stylesheet">
<style>
:root{
  --navy:#26318f;
  --owners:#2f3c9e;
  --buyers:#1e2d6a;
  --lenders:#0d1a44;
  --brokers:#0b3560;
  --grey-bg:#f5f5f5;
  --text:#333;
  --muted:#555;
  --footer:#333333;
  --footer-bottom:#0c0c0c;
  --footer-text:#9a9a9a;
  --star:#1e63b6;
  --white:#fff;
}
*{margin:0;padding:0;box-sizing:border-box}
html,body{width:1200px;height:2397px;overflow:hidden}
body{font-family:'Roboto',sans-serif;color:var(--text);background:var(--white);position:relative}
.abs{position:absolute}

/* hero */
.hero{left:0;top:0;width:1200px;height:523px;background:linear-gradient(180deg,#8fa6c0 0%,#b9c8d8 35%,#6f8196 62%,#3f5a3a 78%,#5b6066 100%)}
.hero-shade{left:0;top:0;width:1200px;height:523px;background:rgba(20,30,50,.25)}
.logo-box{left:137px;top:0;width:114px;height:96px;background:var(--white);display:flex;flex-direction:column;align-items:center;justify-content:center;gap:6px}
.logo-mark{width:22px;height:22px;background:var(--navy)}
.logo-name{font-size:9px;font-weight:500;color:var(--navy);text-align:center;line-height:1.15;letter-spacing:.5px}
.nav a{position:absolute;top:40px;color:var(--white);font-size:12px;font-weight:700;text-decoration:none;letter-spacing:.2px}
.hero-kicker{left:0;top:233px;width:1200px;text-align:center;color:var(--white);font-size:19px;font-weight:700;letter-spacing:.3px}
.hero-line{top:245px;height:2px;background:var(--white)}
.hero-tagline{left:0;top:286px;width:1200px;text-align:center;color:var(--white);font-size:38px;font-weight:300}

/* audience tiles */
.tile{top:460px;width:221px;height:142px;color:var(--white);display:flex;flex-direction:column;align-items:center;padding-top:36px}
.tile svg{width:40px;height:40px}
.tile span{margin-top:16px;font-size:19px;font-weight:400}
.tile-owners{left:137px;background:var(--owners)}
.tile-buyers{left:371px;background:var(--buyers)}
.tile-lenders{left:606px;background:var(--lenders)}
.tile-brokers{left:842px;background:var(--brokers)}

/* who we are */
.about{left:0;top:628px;width:1200px;height:450px;background:var(--grey-bg)}
.about-frame{left:150px;top:687px;width:314px;height:365px;background:#dde3ea}
.about-photo{left:137px;top:671px;width:314px;height:365px;background:linear-gradient(160deg,#2f7fc7 0%,#9fd0f3 35%,#e9f4fc 50%,#4f8ac4 75%,#5a7d3a 100%)}
.about-title{left:519px;top:706px;font-size:25px;font-weight:400;color:#222}
.about-text{left:526px;top:750px;width:510px;font-size:11.5px;line-height:19px;color:var(--muted)}
.btn{background:var(--navy);color:var(--white);font-size:11.5px;display:flex;align-items:center;justify-content:center;text-transform:uppercase}
.about-btn{left:526px;top:944px;width:97px;height:36px}

/* clients */
.clients-title{left:0;top:1106px;width:1200px;text-align:center;font-size:19px;font-weight:400;color:#444}
.client{font-size:11px;font-weight:700;color:#222;display:flex;align-items:center;gap:14px}
.client svg{width:17px;height:17px;fill:var(--star)}

/* contact band */
.contact-band{left:0;top:1312px;width:1200px;height:662px;background:linear-gradient(180deg,#3e4f8c 0%,#4a5c96 45%,#34437a 70%,#3a4578 100%)}
.contact-overlay{left:0;top:1312px;width:1200px;height:662px;background:rgba(35,45,130,.55)}
.quote{left:0;top:1366px;width:1200px;text-align:center;color:var(--white);font-size:29px;font-weight:500}
.info{left:0;width:1200px;text-align:center;color:var(--white)}
.info a{color:var(--white)}
.form-card{left:392px;top:1588px;width:449px;height:417px;background:var(--white);z-index:5}
.form-title{left:392px;top:1622px;width:449px;text-align:center;font-size:19px;color:#222;font-weight:400;z-index:6}
.field{left:435px;width:359px;height:37px;border:1px solid #9aa0a8;font-size:11px;color:#555;padding:12px 15px;text-transform:uppercase;z-index:6}
.form-btn{left:550px;top:1948px;width:113px;height:34px;z-index:6}

/* footer */
.footer{left:0;top:1974px;width:1200px;height:362px;background:var(--footer);z-index:1}
.footer-bottom{left:0;top:2336px;width:1200px;height:61px;background:var(--footer-bottom);color:var(--footer-text);font-size:11px;display:flex;align-items:center;justify-content:center;z-index:1}
.fcol{z-index:2}
.fcol h3{font-size:19px;font-weight:400;color:var(--white);margin-bottom:22px}
.fcol li{list-style:none;font-size:11px;color:var(--footer-text);height:27px}
.social li{display:flex;align-items:center;gap:18px;height:29px}
.social .dot{width:10px;height:10px;background:var(--white);border-radius:50%}
</style>
</head>
<body>

<div class="abs hero" role="img" aria-label="City skyline of glass office towers with trees and a plaza below"></div>
<div class="abs hero-shade"></div>

<div class="abs logo-box">
  <div class="logo-mark"></div>
  <div class="logo-name">BRIGHTLANE<br>COUNSEL GROUP</div>
</div>

<nav class="nav">
  <a href="#" style="left:548px">WHO WE ARE</a>
  <a href="#" style="left:663px">WHAT WE DO</a>
  <a href="#" style="left:778px">CONTACT US</a>
  <a href="#" style="left:895px">INDUSTRY EVENTS CALENDAR</a>
</nav>

<div class="abs hero-line" style="left:328px;width:127px"></div>
<div class="abs hero-line" style="left:743px;width:128px"></div>
<div class="abs hero-kicker">BRIGHTLANE COUNSEL GROUP</div>
<div class="abs hero-tagline">EXPERT - EXPERIENCED - COST EFFECTIVE</div>

<a class="abs tile tile-owners">
  <svg viewBox="0 0 40 40" fill="none" stroke="#fff" stroke-width="1.8"><path d="M6 20 20 8l14 12"/><path d="M10 17v15h20V17"/><rect x="17" y="23" width="6" height="9"/></svg>
  <span>FOR OWNERS</span>
</a>
<a class="abs tile tile-buyers">
  <svg viewBox="0 0 40 40" fill="none" stroke="#fff" stroke-width="1.8"><circle cx="17" cy="17" r="10"/><path d="M24 24l10 10"/></svg>
  <span>FOR BUYERS</span>
</a>
<a class="abs tile tile-lenders">
  <svg viewBox="0 0 40 40" fill="none" stroke="#fff" stroke-width="1.8"><rect x="8" y="6" width="24" height="28"/><path d="M13 13h14M13 19h14M13 25h8"/></svg>
  <span>FOR LENDERS</span>
</a>
<a class="abs tile tile-brokers">
  <svg viewBox="0 0 40 40" fill="none" stroke="#fff" stroke-width="1.8"><rect x="6" y="13" width="28" height="19"/><path d="M15 13V8h10v5M6 21h28"/></svg>
  <span>FOR BROKERS</span>
</a>

<section>
  <div class="abs about"></div>
  <div class="abs about-frame"></div>
  <div class="abs about-photo" role="img" aria-label="Upward view of glass skyscrapers against a bright sky with trees at the edge"></div>
  <h2 class="abs about-title">WHO WE ARE</h2>
  <div class="abs about-text">
    <p>Brightlane Counsel Group is an independent consulting firm offering practical, hands-on assistance to the commercial real estate and commercial mortgage lending industries.&nbsp; We specialize in financial analysis, underwriting and financial due diligence.</p>
    <p>Working with us, you get top notch help when you need it – and only when you need it – one project at a time</p>
    <p>.</p>
    <p>Brightlane Counsel Group has been providing expert, experienced and cost-effective service to the commercial real estate and commercial mortgage industries since 2001.&nbsp; We have worked on projects across Canada and the United States, and in every major property type.</p>
  </div>
  <a class="abs btn about-btn">Readmore</a>
</section>

<section>
  <h2 class="abs clients-title">OUR CLIENTS INCLUDE</h2>
  <div class="abs client" style="left:170px;top:1161px"><svg viewBox="0 0 20 20"><path d="M10 1l2.6 6 6.4.5-4.9 4.2 1.5 6.3L10 14.6 4.4 18l1.5-6.3L1 7.5 7.4 7z"/></svg>CHARTERED BANKS</div>
  <div class="abs client" style="left:170px;top:1194px"><svg viewBox="0 0 20 20"><path d="M10 1l2.6 6 6.4.5-4.9 4.2 1.5 6.3L10 14.6 4.4 18l1.5-6.3L1 7.5 7.4 7z"/></svg>MORTGAGE BANKERS</div>
  <div class="abs client" style="left:170px;top:1236px"><svg viewBox="0 0 20 20"><path d="M10 1l2.6 6 6.4.5-4.9 4.2 1.5 6.3L10 14.6 4.4 18l1.5-6.3L1 7.5 7.4 7z"/></svg>PUBLIC REITS &amp; REOCS</div>
  <div class="abs client" style="left:460px;top:1162px"><svg viewBox="0 0 20 20"><path d="M10 1l2.6 6 6.4.5-4.9 4.2 1.5 6.3L10 14.6 4.4 18l1.5-6.3L1 7.5 7.4 7z"/></svg>PRIVATE EQUITY FIRMS</div>
  <div class="abs client" style="left:460px;top:1201px"><svg viewBox="0 0 20 20"><path d="M10 1l2.6 6 6.4.5-4.9 4.2 1.5 6.3L10 14.6 4.4 18l1.5-6.3L1 7.5 7.4 7z"/></svg>FAMILY-OWNED REAL ESTATE&nbsp; INVESTMENT COMPANIES</div>
  <div class="abs client" style="left:460px;top:1239px"><svg viewBox="0 0 20 20"><path d="M10 1l2.6 6 6.4.5-4.9 4.2 1.5 6.3L10 14.6 4.4 18l1.5-6.3L1 7.5 7.4 7z"/></svg>LIFE INSURANCE COMPANIES</div>
  <div class="abs client" style="left:842px;top:1162px"><svg viewBox="0 0 20 20"><path d="M10 1l2.6 6 6.4.5-4.9 4.2 1.5 6.3L10 14.6 4.4 18l1.5-6.3L1 7.5 7.4 7z"/></svg>PENSION FUNDS</div>
  <div class="abs client" style="left:842px;top:1201px"><svg viewBox="0 0 20 20"><path d="M10 1l2.6 6 6.4.5-4.9 4.2 1.5 6.3L10 14.6 4.4 18l1.5-6.3L1 7.5 7.4 7z"/></svg>NON-BANK LENDERS</div>
  <div class="abs client" style="left:842px;top:1239px"><svg viewBox="0 0 20 20"><path d="M10 1l2.6 6 6.4.5-4.9 4.2 1.5 6.3L10 14.6 4.4 18l1.5-6.3L1 7.5 7.4 7z"/></svg>BROKERAGE FIRMS</div>
</section>

<section>
  <div class="abs contact-band" role="img" aria-label="Business plaza with modern office buildings under a cloudy sky, tinted blue"></div>
  <div class="abs contact-overlay"></div>
  <p class="abs quote">“Reputation is the currency of the 21st century”</p>
  <p class="abs info" style="top:1447px;font-size:14px">For more information please call us at</p>
  <p class="abs info" style="top:1472px;font-size:27px;font-weight:300">905-555-0148<span style="font-size:14px">.</span></p>
  <p class="abs info" style="top:1522px;font-size:14px">Email:&nbsp; Dana Whitfield at <a href="#">dana.whitfield@brightlanecounselgroup.ca</a>, or click below.</p>
</section>

<footer>
  <div class="abs footer"></div>
  <div class="abs fcol" style="left:147px;top:2070px">
    <h3>Company</h3>
    <ul><li>Contact us</li><li>Terms and Conditions</li><li>Careers</li><li>Privacy Policy</li><li>Support</li></ul>
  </div>
  <div class="abs fcol" style="left:388px;top:2071px">
    <h3>Solutions</h3>
    <ul><li>Design Management</li><li>Toolkits</li><li>Project Review</li><li>Value Management</li><li>Project Certification</li><li>Project Bid Team Assistance</li><li>Forum</li></ul>
  </div>
  <div class="abs fcol" style="left:642px;top:2070px">
    <h3>Address</h3>
    <ul>
      <li style="height:19px">Addressname1</li><li>Address name2</li>
      <li style="margin-top:11px">Email: info@website.com</li>
      <li style="margin-top:11px">Phone : +123 123123</li>
    </ul>
  </div>
  <div class="abs fcol social" style="left:957px;top:2070px">
    <h3 style="margin-bottom:26px">Social</h3>
    <ul>
      <li><span class="dot"></span>Chirpline</li>
      <li><span class="dot"></span>Friendpage</li>
      <li><span class="dot"></span>Snapgallery</li>
      <li><span class="dot"></span>Circles Plus</li>
    </ul>
  </div>
  <div class="abs footer-bottom">© 2018 Copyrights All rights reserved | www.brightlanecounselgroup.ca</div>
</footer>

<form class="contact-form">
  <div class="abs form-card"></div>
  <h3 class="abs form-title">CONTACT NOW</h3>
  <div class="abs field" style="top:1665px">Name</div>
  <div class="abs field" style="top:1713px">Email Address</div>
  <div class="abs field" style="top:1764px">Phone Number</div>
  <div class="abs field" style="top:1814px;height:109px">Message</div>
  <a class="abs btn form-btn">Contact Now</a>
</form>

</body>
</html>
```